The Perfect Business Card for Vantorell

I am looking for a business card which beautifully incorporates my logo, reflects my business and looks special, elegant and clean.

```html
<!DOCTYPE html>
<html lang="en">
<head>
<meta charset="utf-8">
<title>Vantorell Business Card</title>
<link href="https://fonts.googleapis.com/css2?family=Montserrat:wght@400;700&display=swap" rel="stylesheet">
<style>
  :root {
    --page-bg: #ffffff;
    --card-bg: #f6fafc;
    --pattern-light: #f7fbfd;
    --pattern-tone: #eff4f4;
    --card-border: #7d838b;
    --brand-green: #6a8a33;
    --text-dark: #000000;
  }
  html, body {
    margin: 0;
    padding: 0;
    width: 1200px;
    height: 1000px;
    overflow: hidden;
    background: var(--page-bg);
    font-family: "Montserrat", sans-serif;
  }
  .canvas {
    position: relative;
    width: 1200px;
    height: 1000px;
  }
  .card {
    position: absolute;
    left: 273px;
    width: 654px;
    height: 394px;
    box-sizing: border-box;
    border: 1px solid var(--card-border);
    background: var(--card-bg);
    overflow: hidden;
  }
  .card--front { top: 90px; }
  .card--back { top: 516px; }
  .card__pattern {
    position: absolute;
    inset: 0;
    background:
      radial-gradient(circle at 50% 50%, var(--pattern-light) 0%, transparent 70%),
      linear-gradient(180deg, var(--pattern-tone), var(--pattern-light) 50%, var(--pattern-tone));
  }
  .brand {
    position: absolute;
    inset: 0;
    display: flex;
    align-items: center;
    justify-content: center;
    gap: 18px;
    padding-bottom: 0;
  }
  .brand__dot {
    width: 30px;
    height: 30px;
    border-radius: 50%;
    background: var(--brand-green);
  }
  .brand__name {
    font-size: 48px;
    font-weight: 400;
    letter-spacing: 1px;
    color: var(--brand-green);
    line-height: 1;
  }
  .contact {
    position: absolute;
    left: 0;
    right: 0;
    text-align: center;
    color: var(--text-dark);
  }
  .contact__name {
    top: 84px;
    margin: 0;
    font-size: 27px;
    font-weight: 700;
    line-height: 36px;
  }
  .contact__details {
    top: 176px;
    margin: 0;
    padding: 0;
    list-style: none;
    font-size: 18.5px;
    font-weight: 400;
    line-height: 33.7px;
  }
</style>
</head>
<body>
<main class="canvas">
  <section class="card card--front">
    <div class="card__pattern" role="img" aria-label="Faint repeating pattern of outdoor travel icons: folded maps, backpacks and compasses"></div>
    <div class="brand">
      <span class="brand__dot"></span>
      <span class="brand__name">Vantorell</span>
    </div>
  </section>

  <section class="card card--back">
    <div class="card__pattern" role="img" aria-label="Faint repeating pattern of outdoor travel icons: folded maps, backpacks and compasses"></div>
    <h1 class="contact contact__name">Daniel Rowe</h1>
    <ul class="contact contact__details">
      <li>(555) 014-782</li>
      <li>daniel@vantorell.com</li>
      <li>www.vantorell.com</li>
      <li>48 Elm Road, US</li>
    </ul>
  </section>
</main>
</body>
</html>
```